Natural deodorant label

Natural clean deodorant line. Need modernize label which can be sized for both the regular and travel size deodorants. 2.75 x 3" and 1x2". Important to highlight no baking soda and its natural. Also has no aluminum, preservatives, nor chemicals. Its gender inclusive and safe for all ages. Please see website at www.lorvatide.com. will attach current label. Will need a label that i would be able to update with new scents as they come. Want a clean look.

Target Market(s)

the working mother/wife that lives a clean healthy life and pushes that for her family

Industry/Entity Type

health and beauty/deodorant/natural

Colors

Designer to choose colors to be used in the design.

Requirements
Must have
• No baking soda and gender inclusive on label. Clean look. Very little to no picture art.
Nice to have
• Potentially a different color representing the different scents. A brief description of the deodorant scent underneath the scent name. This can be found under the drop down menu titled solvane deodorant scents on the website www.lorvatide.com. Area on front label for a small barcode.
Should not have
• misspelled words; dark label

```html
<!DOCTYPE html>
<html lang="en">
<head>
<meta charset="utf-8">
<title>Solvane Island Breeze Deodorant Label</title>
<link href="https://fonts.googleapis.com/css2?family=Raleway:wght@300;700&family=Libre+Baskerville:wght@400;700&display=swap" rel="stylesheet">
<style>
  :root {
    --page-bg: #ececec;
    --label-bg: #f4f8f7;
    --gold: #d6c27a;
    --gold-badge: #d4c184;
    --ink: #1a1a1a;
    --black-badge: #111111;
    --leaf-light: #c9dca6;
    --leaf-mid: #9fbd6e;
  }
  * { box-sizing: border-box; margin: 0; padding: 0; }
  html, body {
    width: 1200px;
    height: 1000px;
    overflow: hidden;
    background: var(--page-bg);
  }
  .label {
    position: absolute;
    left: 360px;
    top: 120px;
    width: 480px;
    height: 760px;
    background: var(--label-bg);
    color: var(--ink);
    font-family: "Libre Baskerville", serif;
  }
  .label__frame {
    position: absolute;
    left: 40px;
    top: 36px;
    right: 24px;
    bottom: 36px;
    border: 3px solid var(--gold);
  }
  .leaves {
    position: absolute;
    border-radius: 50% 10% 50% 10%;
    background: radial-gradient(circle at 40% 40%, var(--leaf-light), var(--leaf-mid));
    opacity: 0.85;
  }
  .leaves--top-left {
    left: 0;
    top: 70px;
    width: 92px;
    height: 150px;
  }
  .leaves--bottom-right {
    right: 0;
    top: 420px;
    width: 110px;
    height: 160px;
    border-radius: 10% 50% 10% 50%;
  }
  .brand {
    position: absolute;
    left: 0;
    right: 0;
    top: 92px;
    text-align: center;
  }
  .brand__dot {
    display: block;
    width: 52px;
    height: 52px;
    margin: 0 auto 14px;
    border-radius: 50%;
    background: var(--ink);
  }
  .brand__name {
    font-size: 24px;
    font-weight: 400;
    letter-spacing: 0.5px;
    color: var(--ink);
  }
  .product-name {
    position: absolute;
    left: 0;
    right: 0;
    top: 258px;
    text-align: center;
    font-family: "Raleway", sans-serif;
    font-weight: 300;
    font-size: 64px;
    letter-spacing: 1px;
  }
  .scent-name {
    position: absolute;
    left: 0;
    right: 0;
    top: 366px;
    text-align: center;
    font-family: "Raleway", sans-serif;
    font-weight: 700;
    font-size: 18px;
    letter-spacing: 0.5px;
  }
  .badge {
    position: absolute;
    left: 42px;
    width: 84px;
    padding: 10px 8px;
    font-family: "Libre Baskerville", serif;
    font-weight: 700;
    font-size: 10px;
    line-height: 1.25;
    text-transform: uppercase;
  }
  .badge--inclusive {
    top: 478px;
    background: var(--black-badge);
    color: var(--gold-badge);
  }
  .badge--no-soda {
    top: 542px;
    background: var(--gold-badge);
    color: var(--ink);
  }
  .label__footer {
    position: absolute;
    left: 0;
    right: 0;
    top: 622px;
    text-align: center;
    font-size: 17px;
    line-height: 1.4;
    text-transform: uppercase;
  }
</style>
</head>
<body>
  <main class="label">
    <div class="leaves leaves--top-left" role="img" aria-label="Sprig of green leaves"></div>
    <div class="leaves leaves--bottom-right" role="img" aria-label="Sprig of green leaves"></div>
    <div class="label__frame"></div>

    <header class="brand">
      <span class="brand__dot"></span>
      <span class="brand__name">Lorvatide</span>
    </header>

    <h1 class="product-name">SOLVANE</h1>
    <p class="scent-name">ISLAND BREEZE</p>

    <p class="badge badge--inclusive">Gender<br>Inclusive</p>
    <p class="badge badge--no-soda">No<br>Baking<br>Soda</p>

    <footer class="label__footer">
      <p>Naturally Refreshing</p>
      <p>Net Wt 2.5 oz (70g)</p>
    </footer>
  </main>
</body>
</html>
```